Postcard Design

Need a post card looking to attract brides and interns at a trade show. love to use my logo and an image or two of past events and maybe a background pic fading behind the verbage. pick whatever images you think work.
Gilded Galas
couture coordination for fashionable events
Marla Quintrell, MBC
marla@gilded-galas.com

```html
<!DOCTYPE html>
<html lang="en">
<head>
<meta charset="utf-8">
<title>Gilded Galas Postcard</title>
<link rel="stylesheet" href="https://fonts.googleapis.com/css2?family=Source+Sans+3:wght@400;600&display=swap">
<style>
  :root {
    --orange: #f5a623;
    --orange-deep: #ef9a12;
    --orange-soft: #fbc764;
    --ink: #3a3a3a;
    --grey: #6b6b6b;
    --pink: #f6c4cf;
    --paper: #ffffff;
    --page: #ffffff;
    --rule: #bdbdbd;
  }
  * { box-sizing: border-box; margin: 0; padding: 0; }
  html, body { width: 880px; height: 1200px; overflow: hidden; background: var(--page); }
  body { position: relative; font-family: "Source Sans 3", sans-serif; color: var(--ink); }

  .card {
    position: absolute; left: 24px; width: 826px;
    background: var(--paper);
    box-shadow: 4px 5px 10px rgba(0,0,0,.35);
  }
  .card--front { top: 30px; height: 540px; }
  .card--back { top: 595px; height: 560px; }

  /* Front */
  .brand { position: absolute; top: 26px; left: 0; right: 0; text-align: center; }
  .brand__name { font-size: 44px; font-weight: 400; color: var(--ink); letter-spacing: 1px; line-height: 1.1; }
  .brand__tag { font-size: 14px; color: var(--grey); letter-spacing: 3px; margin-top: 4px; }

  .gallery-strip { position: absolute; top: 170px; left: 30px; right: 16px; height: 150px; background: var(--orange); }
  .photo { position: absolute; border: 5px solid var(--orange); }
  .photo--couple { top: 128px; left: 40px; width: 230px; height: 232px; background: linear-gradient(135deg,#2a2422,#6a5a52 55%,#d9cfc8); }
  .photo--bouquet { top: 128px; left: 286px; width: 300px; height: 232px; background: radial-gradient(circle at 50% 50%,#f1ede0,#c4c9a2 55%,#6e7850); }
  .photo--portrait { top: 128px; left: 602px; width: 208px; height: 232px; background: linear-gradient(160deg,#7d9a5c,#e6e2dc 55%,#b9b3aa); }

  .sub-brand { position: absolute; top: 366px; left: 0; right: 0; text-align: center; }
  .sub-brand__name { font-size: 46px; color: var(--orange-deep); line-height: 1; }
  .sub-brand__line { font-size: 15px; color: var(--grey); letter-spacing: 4px; line-height: 1.2; }
  .sub-brand__note { font-size: 13px; color: var(--grey); line-height: 1.3; font-style: italic; }

  .front-band { position: absolute; left: 0; right: 0; bottom: 14px; height: 62px; background: linear-gradient(180deg,var(--orange-soft),var(--orange)); }

  /* Back */
  .photo--flowers { top: 18px; left: 26px; width: 262px; height: 222px; border: none; background: radial-gradient(circle at 45% 50%,#e86a2a,#c94a1e 40%,#efe9e2 75%); }
  .contact { position: absolute; top: 40px; left: 312px; line-height: 1.15; }
  .contact__name { font-size: 30px; font-weight: 600; color: var(--orange-deep); }
  .contact__tag { font-size: 25px; color: var(--grey); }
  .contact__person, .contact__email { font-size: 24px; color: var(--grey); }
  .contact__mark { position: absolute; top: 186px; left: 606px; width: 26px; height: 26px; background: var(--orange); }
  .postage { position: absolute; top: 20px; left: 658px; width: 150px; height: 160px; background: var(--pink); }
  .postage span { position: absolute; top: 34px; left: 0; right: 0; text-align: center; font-size: 17px; color: var(--grey); line-height: 1.2; }

  .about { position: absolute; top: 260px; left: 26px; width: 490px; height: 286px; background: var(--orange); padding: 22px 24px; color: #fff; font-size: 22px; line-height: 1.3; }
  .address { position: absolute; top: 260px; left: 516px; width: 300px; height: 270px; border: 1px solid var(--rule); border-left: none; background: var(--paper); }
  .address span { position: absolute; top: 36px; left: 20px; right: 0; text-align: center; font-size: 18px; color: var(--ink); }
</style>
</head>
<body>
  <section class="card card--front">
    <div class="brand">
      <div class="brand__name">Gilded Galas</div>
      <div class="brand__tag">weddings · fashionable events</div>
    </div>
    <div class="gallery-strip"></div>
    <div class="photo photo--couple" role="img" aria-label="Photo of a bride and groom's hands with a bracelet"></div>
    <div class="photo photo--bouquet" role="img" aria-label="Photo of a white and green bridal bouquet"></div>
    <div class="photo photo--portrait" role="img" aria-label="Photo of a wedding couple outdoors"></div>
    <div class="sub-brand">
      <div class="sub-brand__name">solenne</div>
      <div class="sub-brand__line">event planning</div>
      <div class="sub-brand__note">a Gilded Galas company</div>
    </div>
    <div class="front-band"></div>
  </section>

  <section class="card card--back">
    <div class="photo photo--flowers" role="img" aria-label="Photo of an orange rose wedding bouquet"></div>
    <div class="contact">
      <div class="contact__name">Gilded Galas</div>
      <div class="contact__tag">couture coordination<br>for fashionable events</div>
      <div class="contact__person">Marla Quintrell, MBC</div>
      <div class="contact__email">marla@gilded-galas.com</div>
    </div>
    <div class="contact__mark"></div>
    <div class="postage"><span>Postage<br>Area</span></div>
    <div class="about">Solenne is your day-of, go-to person that ensures all your vendors are fulfilling their promises of over-the-top service to you. It's important to us that you enjoy your event, so we promise to represent you and only. We look out for your best interests and act on your behalf to ensure your event goes off without a hitch.</div>
    <div class="address"><span>Address Area</span></div>
  </section>
</body>
</html>
```